Flyer for Consulting Services (PM+Dev-Lead)

• The attached document describes consulting services for StartUps or young companies with a digital buisness model. We provide services for product management and development lead/scrum master. The target group of the flyer (i.e. who reads that flyer) is CEOs of Startups, Founders, Investors, Business Angle.s
• The task is to design an A4 flyer with one page layout (one pager) mostly for electronic destribution (printing second choice). There have to be two versions according given input: one in German and one in English with same layout. Preferably a format which allows us to adjust wording (e.g. Word, MS Publisher, …)
The final design should deliver professionality on one side and agility/StartUp mentality on the other side.

```html
<!DOCTYPE html>
<html lang="en">
<head>
<meta charset="utf-8">
<title>Consulting Flyer – Product Management and Development</title>
<link rel="stylesheet" href="https://fonts.googleapis.com/css2?family=Open+Sans:wght@300;400;600;700;800&display=swap">
<style>
  :root{
    --blue:#3aa9e4;
    --purple:#4b2c98;
    --ink:#2b2b33;
    --muted:#55555f;
    --line:#b8b8c2;
    --paper:#ffffff;
    --contact-bg:#f3f3f6;
    --grad:linear-gradient(90deg,#3db2e8 0%,#4a7fd0 50%,#4e3499 100%);
  }
  *{box-sizing:border-box;margin:0;padding:0}
  html,body{width:707px;height:1200px;overflow:hidden;background:var(--paper)}
  body{font-family:"Open Sans",Arial,sans-serif;color:var(--ink);position:relative}

  .header{position:absolute;left:0;top:0;width:707px;height:88px;background:var(--grad);color:#fff;display:flex;align-items:center}
  .header-col{flex:1;text-align:center;padding:0 8px}
  .header-col + .header-col{border-left:1px solid rgba(255,255,255,.55)}
  .header-name{font-weight:700;font-size:13px;white-space:nowrap}
  .header-role{font-size:11.5px;font-weight:400;opacity:.95;margin-top:2px;white-space:nowrap}

  .hero{position:absolute;left:28px;top:108px;width:668px;height:408px;border-bottom-left-radius:170px;
        background:linear-gradient(135deg,#e9e4dc 0%,#cfc3b5 45%,#8a7c70 75%,#3a3d4a 100%)}

  .intro{position:absolute;left:0;top:526px;width:707px;text-align:center}
  .intro-you{color:var(--blue);font-weight:700;font-size:24px;line-height:1.25}
  .intro-line{font-size:13px;line-height:21px;text-transform:uppercase;color:var(--ink)}
  .intro-line strong{font-weight:700}
  .partner{display:flex;align-items:center;justify-content:center;gap:16px;margin-top:12px}
  .partner::before,.partner::after{content:"";width:105px;height:1px;background:var(--line)}
  .partner-text{font-weight:300;font-size:19px;text-transform:uppercase}
  .claim{color:var(--purple);font-size:21px;font-weight:400;margin-top:6px;text-transform:uppercase}
  .claim strong{font-weight:800}

  .section-title{color:var(--blue);font-weight:700;font-size:22px;line-height:1.2;text-transform:uppercase;margin-bottom:10px}
  .bullets{list-style:none}
  .bullets li{position:relative;padding-left:16px;font-size:11.5px;line-height:16px;color:var(--muted);margin-bottom:14px}
  .bullets li::before{content:"";position:absolute;left:2px;top:6px;width:5px;height:5px;border-radius:50%;background:var(--purple)}

  .col-left{position:absolute;left:28px;top:718px;width:290px}
  .col-left .if-wanted{margin-top:24px}
  .col-left .bullets.tight li{margin-bottom:10px}
  .col-right{position:absolute;left:355px;top:718px;width:330px}

  .why{position:absolute;left:355px;top:920px;width:352px;height:152px;border-top-left-radius:34px;background:var(--grad);color:#fff;padding:16px 20px 0 26px}
  .why-title{font-weight:700;font-size:22px;text-transform:uppercase;margin-bottom:10px}
  .why-item{display:flex;gap:8px;font-size:12px;line-height:17px;margin-bottom:14px}
  .why-item svg{flex:none;margin-top:2px}

  .contact{position:absolute;left:355px;top:1072px;width:352px;height:110px;background:var(--contact-bg);padding:10px 0 0 22px}
  .contact-title{color:var(--purple);font-weight:700;font-size:21px;text-transform:uppercase}
  .contact-people{display:flex;margin-top:6px}
  .person{padding-right:10px}
  .person + .person{border-left:1px solid var(--line);padding-left:10px}
  .person-name{font-weight:700;font-size:12.5px;color:var(--ink)}
  .person-line{display:flex;align-items:center;gap:5px;font-size:10.5px;color:var(--muted);font-style:italic;line-height:17px;white-space:nowrap}

  .rule-left{position:absolute;left:0;top:1186px;width:355px;height:3px;background:var(--blue)}
  .rule-right{position:absolute;left:355px;top:1182px;width:352px;height:4px;background:var(--purple)}
</style>
</head>
<body>
  <header class="header">
    <div class="header-col">
      <div class="header-name">Malte HansbergJens Korbach &amp; Velmoryx GmbH</div>
      <div class="header-role">Agile Product Manager</div>
    </div>
    <div class="header-col">
      <div class="header-name">Jens Korbach &amp; Velmoryx GmbH</div>
      <div class="header-role">Agile Product ManagerScrum Master, Dev-Lead</div>
    </div>
  </header>

  <div class="hero" role="img" aria-label="Photo of a consultant meeting two young founders at a desk in a bright office"></div>

  <section class="intro">
    <div class="intro-you">YOU ...</div>
    <p class="intro-line">Have a <strong>digital business idea?</strong></p>
    <p class="intro-line">Already obtained <strong>a funding?</strong></p>
    <p class="intro-line">Are you looking for <strong>experienced</strong> support for <strong>product development?</strong></p>
    <div class="partner"><span class="partner-text">We are your partner for</span></div>
    <p class="claim"><strong>Product management</strong> and <strong>development!</strong></p>
  </section>

  <section class="col-left">
    <h2 class="section-title">We ...</h2>
    <ul class="bullets">
      <li>Take over interim roles as: product owner,<br>scrum master, and dev-lead</li>
      <li>Create your development team, optionally<br>with offshore/nearshore locations</li>
      <li>Setup the cloud environment for your solution<br>and support its operations</li>
      <li>Jointly establish an agile/lean mindset including<br>corresponding procedures</li>
    </ul>
    <h2 class="section-title if-wanted">If wanted, ...</h2>
    <ul class="bullets tight">
      <li>Together we evolve your strategic orientation</li>
      <li>Support you in architecture and technology design</li>
      <li>Train you in product management and in creating a<br>Scalable agile organisation</li>
    </ul>
  </section>

  <section class="col-right">
    <h2 class="section-title">Your benefits</h2>
    <ul class="bullets">
      <li>You focus on your ideas and your business model</li>
      <li>You receive a professional realization of your ideas<br>in quality, time and budget</li>
      <li>Our lean/agile mindset supports your start-up<br>mentality and your commercial success</li>
    </ul>
  </section>

  <section class="why">
    <h2 class="why-title">Why us?</h2>
    <div class="why-item">
      <svg width="13" height="13" viewBox="0 0 14 14"><circle cx="7" cy="7" r="6" fill="none" stroke="#fff" stroke-width="1.3"/><path d="M4 7.2l2 2 4-4.2" fill="none" stroke="#fff" stroke-width="1.3"/></svg>
      <span>Combined expertise in product management,<br>development, and operations</span>
    </div>
    <div class="why-item">
      <svg width="13" height="13" viewBox="0 0 14 14"><circle cx="7" cy="7" r="6" fill="none" stroke="#fff" stroke-width="1.3"/><path d="M4 7.2l2 2 4-4.2" fill="none" stroke="#fff" stroke-width="1.3"/></svg>
      <span>Founders with experiences in digital business<br>models and numerous industries</span>
    </div>
  </section>

  <section class="contact">
    <h2 class="contact-title">How to contact us?</h2>
    <div class="contact-people">
      <div class="person">
        <div class="person-name">Malte Hansberg</div>
        <div class="person-line"><svg width="10" height="10" viewBox="0 0 10 10"><path d="M2 1l2 2-1 1.2c.6 1.2 1.6 2.2 2.8 2.8L7 6l2 2-1.2 1.4C4.5 9 1 5.5.6 2.2z" fill="#4b2c98"/></svg>+49-170-55 02 41 19</div>
        <div class="person-line"><svg width="10" height="8" viewBox="0 0 10 8"><rect width="10" height="8" rx="1" fill="#3aa9e4"/><path d="M0 1l5 3.5L10 1" fill="none" stroke="#fff" stroke-width=".9"/></svg>contact@malte-hansberg.de</div>
      </div>
      <div class="person">
        <div class="person-name">Jens Korbach</div>
        <div class="person-line"><svg width="10" height="10" viewBox="0 0 10 10"><path d="M2 1l2 2-1 1.2c.6 1.2 1.6 2.2 2.8 2.8L7 6l2 2-1.2 1.4C4.5 9 1 5.5.6 2.2z" fill="#4b2c98"/></svg>+49-171-6 38 90 27</div>
        <div class="person-line"><svg width="10" height="8" viewBox="0 0 10 8"><rect width="10" height="8" rx="1" fill="#3aa9e4"/><path d="M0 1l5 3.5L10 1" fill="none" stroke="#fff" stroke-width=".9"/></svg>jens.korbach@velmoryx</div>
      </div>
    </div>
  </section>

  <div class="rule-left"></div>
  <div class="rule-right"></div>
</body>
</html>
```